PowerPoint template for my training workshop business

I would like to have a PowerPoint template created using my logo and palette materials created by Brindlework. I train and facilitate workshops using PowerPoint in both corporate and public settings.

I have attached the original design elements to this request.

```html
<!DOCTYPE html>
<html lang="en">
<head>
<meta charset="utf-8">
<title>Workshop &amp; Training Presentation Template</title>
<link rel="stylesheet" href="https://fonts.googleapis.com/css2?family=Oswald:wght@400;500;600&family=Open+Sans:wght@400;600;700&family=Ubuntu:wght@300;400;700&display=swap">
<style>
:root{
  --orange:#f8b134;
  --orange-deep:#f3a11c;
  --orange-soft:#fbc862;
  --ink:#2f3439;
  --slate:#4d555c;
  --grey:#8f969c;
  --mist:#eceef0;
  --paper:#ffffff;
  --stage-top:#45423d;
  --stage-bottom:#1d1f21;
  --board:#2e3033;
}
*{margin:0;padding:0;box-sizing:border-box}
html,body{width:930px;height:1200px;overflow:hidden}
body{background:var(--board);font-family:"Open Sans",sans-serif;color:var(--ink)}
.board{position:relative;width:930px;height:1200px;overflow:hidden}

/* hero */
.hero{position:absolute;left:0;top:0;width:930px;height:642px;background:linear-gradient(160deg,var(--stage-top),var(--stage-bottom))}
.brand{position:absolute;left:30px;top:88px;display:flex;align-items:center;gap:12px}
.brand-mark{width:56px;height:56px;border-radius:50%;border:5px solid var(--orange)}
.brand-name{font-family:"Oswald",sans-serif;font-weight:500;font-size:27px;letter-spacing:1.5px;color:var(--orange);line-height:1.05}
.brand-name small{display:block;font-size:13px;letter-spacing:5px;color:var(--orange);font-weight:500}
.hero-cover{position:absolute;left:360px;top:165px;width:412px;height:258px;box-shadow:0 10px 30px rgba(0,0,0,.5)}
.hero-title{position:absolute;left:30px;top:528px;font-family:"Ubuntu",sans-serif;font-weight:700;font-size:54px;color:#d7d7d7;letter-spacing:-.5px}
.hero-title em{font-style:normal;color:var(--orange)}
.hero-sub{position:absolute;left:31px;top:590px;font-family:"Ubuntu",sans-serif;font-weight:300;font-size:29px;color:#d7d7d7;letter-spacing:1px}

/* grid */
.deck{position:absolute;left:5px;top:653px;width:920px;display:grid;grid-template-columns:repeat(5,176px);grid-auto-rows:99px;column-gap:10px;row-gap:9px}
.slide{position:relative;overflow:hidden;background:var(--paper)}
.slide svg.cover{width:176px;height:99px;display:block}
.abs{position:absolute}
.kick{position:absolute;left:8px;top:6px;display:flex;align-items:center;gap:1.5px;font-size:2.2px;color:var(--grey)}
.kick i{display:inline-block;width:2px;height:2px;background:var(--orange)}
.kick i:last-of-type{background:var(--grey);margin-right:2px}
.ttl{position:absolute;left:8px;top:10px;font-family:"Oswald",sans-serif;font-weight:500;font-size:8.5px;line-height:1.1;color:var(--ink)}
.ttl.light{color:#fff}
.tag{position:absolute;right:6px;top:4px;display:flex;align-items:center;gap:1.5px;font-family:"Oswald",sans-serif;font-size:2.6px;color:var(--orange);background:#fff;padding:1px 2px}
.tag b{width:4px;height:4px;border-radius:50%;border:.8px solid var(--orange)}
.page{position:absolute;right:6px;bottom:5px;width:13px;height:4px;border:.5px solid #d6d9dc;font-size:2px;text-align:right;padding-right:2px;color:var(--grey);line-height:3px}
.t{font-size:2.5px;line-height:1.35;color:var(--grey)}
.t.w{color:#d9dcdf}
.lab{font-size:3.2px;font-weight:700;color:var(--orange);line-height:1.3}
.lab.d{color:var(--ink)}
.lab.w{color:#fff}
.pill{position:absolute;height:4.5px;border-radius:3px;background:var(--orange);font-size:2.2px;color:#fff;text-align:center;line-height:4.5px}
.pill.dark{background:var(--ink)}
.ph{background:linear-gradient(135deg,#d2ccc3,#8f8880)}
.ph-cool{background:linear-gradient(135deg,#c9ced3,#7b838b)}
.ph-dark{background:linear-gradient(135deg,#5a6066,#262a2e)}
.sq{position:absolute;width:7px;height:7px}
.sq.o{background:var(--orange)}
.sq.g{background:var(--grey)}
.sq.k{background:var(--ink)}
.num{font-family:"Oswald",sans-serif;font-size:3px;color:#fff;text-align:center;line-height:7px}
.para{position:absolute;width:22px;height:9px;transform:skewX(-18deg)}
.arrow{position:absolute;height:1px;background:var(--orange)}
.arrow::after{content:"";position:absolute;right:-1px;top:-1.5px;border-left:3px solid var(--orange);border-top:2px solid transparent;border-bottom:2px solid transparent}
.arrow.k,.arrow.k::after{background:var(--ink)}
.arrow.k::after{background:none;border-left-color:var(--ink)}
.year{position:absolute;font-family:"Oswald",sans-serif;font-size:3.4px;color:var(--orange)}
.big{font-family:"Oswald",sans-serif;color:#fff;text-align:center}
</style>
</head>
<body>
<svg width="0" height="0" style="position:absolute" aria-hidden="true">
  <defs>
    <symbol id="cover-slide" viewBox="0 0 400 250">
      <rect width="400" height="250" fill="#cfcac2" role="img" aria-label="Photo of hands writing in an open notebook at a desk"/>
      <path d="M0 92 C70 80 150 100 200 140 C240 172 250 212 236 250 H0 Z" fill="#2f3439" opacity=".88"/>
      <path d="M200 140 C260 120 320 160 400 110 V160 C340 190 280 170 230 175 Z" fill="#fbc862" opacity=".7"/>
      <path d="M0 0 H400 V98 C360 88 330 112 300 134 C270 156 240 150 212 134 C170 110 110 94 0 112 Z" fill="#f8b134"/>
      <rect x="37" y="0" width="100" height="40" rx="3" fill="#fff"/>
      <circle cx="51" cy="18" r="7" fill="none" stroke="#f8b134" stroke-width="2"/>
      <text x="62" y="19" font-family="Oswald, sans-serif" font-weight="500" font-size="9" fill="#f8b134">MARINA HOLT</text>
      <text x="71" y="27" font-family="Oswald, sans-serif" font-weight="500" font-size="4.5" letter-spacing="1.5" fill="#f8b134">COACHING</text>
      <text font-family="Oswald, sans-serif" font-weight="500" font-size="14" fill="#fff"><tspan x="39" y="83">Study nature, love nature, stay close</tspan><tspan x="39" y="100">to nature. It will never fail you.</tspan></text>
      <text font-family="Open Sans, sans-serif" font-size="5" fill="#e6e6e6"><tspan x="39" y="121">A wonderful serenity has taken possession of my entire soul, like these sweet</tspan><tspan x="39" y="131">mornings of spring which I enjoy with my whole heart.</tspan></text>
      <rect x="38" y="161" width="60" height="19" rx="9.5" fill="#1f2326"/>
      <text x="68" y="173" text-anchor="middle" font-family="Open Sans, sans-serif" font-size="6" fill="#fff">Learn Now</text>
    </symbol>
  </defs>
</svg>

<main class="board">
  <section class="hero">
    <div class="brand">
      <span class="brand-mark"></span>
      <span class="brand-name">MARINA HOLT<small>COACHING</small></span>
    </div>
    <svg class="hero-cover" viewBox="0 0 400 250" preserveAspectRatio="none" role="img" aria-label="Cover slide"><use href="#cover-slide"/></svg>
    <h1 class="hero-title">Workshop &amp; <em>Training</em></h1>
    <p class="hero-sub">Presentation Template</p>
  </section>

  <section class="deck">
    <!-- 1 cover -->
    <div class="slide"><svg class="cover" viewBox="0 0 400 250" preserveAspectRatio="xMidYMid slice"><use href="#cover-slide"/></svg></div>

    <!-- 2 table of contents -->
    <div class="slide">
      <div class="kick"><i></i><i></i><i></i>Training Template</div>
      <div class="ttl">Table of Contents</div>
      <span class="tag"><b></b>MARINA HOLT</span>
      <div class="sq g" style="left:18px;top:31px"><div class="num">01</div></div>
      <div class="abs" style="left:28px;top:30px;width:30px"><div class="lab">Description</div><div class="t">Short note on this point.</div></div>
      <div class="sq g" style="left:65px;top:31px"><div class="num">02</div></div>
      <div class="abs" style="left:75px;top:30px;width:30px"><div class="lab">Description</div><div class="t">Short note on this point.</div></div>
      <div class="sq g" style="left:112px;top:31px"><div class="num">03</div></div>
      <div class="abs" style="left:122px;top:30px;width:30px"><div class="lab">Description</div><div class="t">Short note on this point.</div></div>
      <div class="sq o" style="left:18px;top:55px"><div class="num">04</div></div>
      <div class="abs" style="left:28px;top:54px;width:30px"><div class="lab d">Description</div><div class="t">Short note on this point.</div></div>
      <div class="sq o" style="left:65px;top:55px"><div class="num">05</div></div>
      <div class="abs" style="left:75px;top:54px;width:30px"><div class="lab d">Description</div><div class="t">Short note on this point.</div></div>
      <div class="sq o" style="left:112px;top:55px"><div class="num">06</div></div>
      <div class="abs" style="left:122px;top:54px;width:30px"><div class="lab d">Description</div><div class="t">Short note on this point.</div></div>
      <div class="abs ph-dark" style="left:0;top:74px;width:176px;height:25px" role="img" aria-label="Dark photo of a workspace"></div>
      <div class="abs t w" style="left:20px;top:80px;width:120px">A short summary of the session goals sits here.</div>
      <div class="pill" style="left:156px;top:86px;width:12px;background:none;border:.5px solid var(--orange)"></div>
    </div>

    <!-- 3 topic list photos -->
    <div class="slide">
      <div class="kick"><i></i><i></i><i></i>Training Template</div>
      <div class="ttl">Topic List</div>
      <span class="tag"><b></b>MARINA HOLT</span>
      <div class="abs ph" style="left:14px;top:26px;width:46px;height:60px" role="img" aria-label="Photo of a person working at a laptop"></div>
      <div class="abs ph-cool" style="left:65px;top:26px;width:46px;height:60px" role="img" aria-label="Photo of a woman at a desk"></div>
      <div class="abs ph" style="left:116px;top:26px;width:46px;height:60px" role="img" aria-label="Photo of hands holding a phone"></div>
      <div class="abs" style="left:14px;top:74px;width:46px;text-align:center"><div class="lab">Study and Learn</div><div class="t w">Science and Tech</div></div>
      <div class="abs" style="left:65px;top:74px;width:46px;text-align:center"><div class="lab">Study and Learn</div><div class="t w">Art and Design</div></div>
      <div class="abs" style="left:116px;top:74px;width:46px;text-align:center"><div class="lab w">Study and Learn</div><div class="t w">Business</div></div>
      <div class="pill" style="left:27px;top:84px;width:20px">Details</div>
      <div class="pill" style="left:78px;top:84px;width:20px">Details</div>
      <div class="pill dark" style="left:129px;top:84px;width:20px">Details</div>
    </div>

    <!-- 4 topic list icons -->
    <div class="slide">
      <div class="kick"><i></i><i></i><i></i>Training Template</div>
      <div class="ttl">Topic List</div>
      <span class="tag"><b></b>MARINA HOLT</span>
      <div class="abs ph-dark" style="left:0;top:27px;width:176px;height:38px" role="img" aria-label="Dark photo of an office"></div>
      <div class="sq o" style="left:19px;top:37px;width:14px;height:14px;border-radius:2px"></div>
      <div class="sq o" style="left:58px;top:37px;width:14px;height:14px;border-radius:2px"></div>
      <div class="sq g" style="left:97px;top:37px;width:14px;height:14px;border-radius:2px;background:var(--slate)"></div>
      <div class="sq k" style="left:136px;top:37px;width:14px;height:14px;border-radius:2px;background:#151719"></div>
      <div class="abs" style="left:10px;top:67px;width:32px;text-align:center"><div class="lab">Description</div><div class="t">Short note on this point.</div></div>
      <div class="abs" style="left:49px;top:67px;width:32px;text-align:center"><div class="lab">Description</div><div class="t">Short note on this point.</div></div>
      <div class="abs" style="left:88px;top:67px;width:32px;text-align:center"><div class="lab d">Description</div><div class="t">Short note on this point.</div></div>
      <div class="abs" style="left:127px;top:67px;width:32px;text-align:center"><div class="lab d">Description</div><div class="t">Short note on this point.</div></div>
      <div class="page"></div>
    </div>

    <!-- 5 topic section -->
    <div class="slide ph-dark" role="img" aria-label="Dark photo of a meeting room">
      <div class="abs" style="left:82px;top:6px;width:12px;height:12px;border-radius:50%;border:1.5px solid var(--orange)"></div>
      <div class="abs" style="left:0;top:32px;width:176px;text-align:center;font-family:Oswald,sans-serif;font-weight:500;font-size:14px;color:#fff">Topic Section</div>
      <div class="pill" style="left:78px;top:52px;width:20px">Subtitle</div>
      <div class="abs t w" style="left:50px;top:62px;width:90px">▪ A short line about this topic.<br>▪ A short line about this topic.<br>▪ A short line about this topic.<br>▪ A short line about this topic.</div>
    </div>

    <!-- 6 about program -->
    <div class="slide">
      <span class="tag"><b></b>MARINA HOLT</span>
      <div class="abs ph-cool" style="left:16px;top:18px;width:50px;height:46px" role="img" aria-label="Photo of a person with a laptop"></div>
      <div class="abs ph-cool" style="left:50px;top:50px;width:30px;height:30px" role="img" aria-label="Photo of a desk"></div>
      <div class="abs" style="left:36px;top:38px;width:26px;height:26px;background:var(--orange);opacity:.85"></div>
      <div class="kick" style="left:96px;top:24px"><i></i><i></i><i></i>Training Template</div>
      <div class="ttl" style="left:96px;top:28px">About Program</div>
      <div class="abs t" style="left:96px;top:40px;width:64px">A short paragraph that introduces the program goals.</div>
      <div class="abs" style="left:96px;top:54px;width:54px;height:22px;background:#fff;box-shadow:0 1px 3px rgba(0,0,0,.15);padding:3px 4px"><div class="lab">Description</div><div class="t">Short note on this point.</div></div>
      <div class="pill dark" style="left:112px;top:70px;width:18px">Learn More</div>
      <div class="page"></div>
    </div>

    <!-- 7 start creative learning -->
    <div class="slide">
      <span class="tag"><b></b>MARINA HOLT</span>
      <div class="kick" style="top:14px"><i></i><i></i><i></i>Training Template</div>
      <div class="ttl" style="top:18px">Start Creative<br>Learning</div>
      <div class="abs t" style="left:8px;top:42px;width:60px">A short paragraph about creative learning and practice.</div>
      <div class="abs ph-cool" style="left:86px;top:14px;width:82px;height:68px" role="img" aria-label="Photo of a person typing on a laptop"></div>
      <div class="abs" style="left:86px;top:72px;width:70px;height:9px;background:var(--ink)"></div>
      <div class="abs t w" style="left:97px;top:73px;width:56px">Creative thinking inspires ideas. Ideas inspire change.</div>
      <div class="page"></div>
    </div>

    <!-- 8 excellent topic -->
    <div class="slide">
      <span class="tag"><b></b>MARINA HOLT</span>
      <div class="abs ph-cool" style="left:8px;top:6px;width:90px;height:56px" role="img" aria-label="Photo of hands holding a phone at a laptop"></div>
      <div class="abs" style="left:25px;top:50px;width:73px;height:10px;background:var(--orange);padding:1.5px 3px"><div class="lab w" style="font-size:2.6px">Northgate College</div></div>
      <div class="kick" style="top:66px"><i></i><i></i><i></i>Training Template</div>
      <div class="ttl" style="top:70px">Excellent Topic</div>
      <div class="abs" style="left:106px;top:20px;width:60px"><div class="lab">Description</div><div class="t">Short note on this point.</div><div class="lab d" style="margin-top:3px">Data Statistic</div></div>
      <svg class="abs" style="left:114px;top:50px" width="52" height="32" viewBox="0 0 52 32" role="img" aria-label="Bar chart">
        <line x1="0" y1="28" x2="52" y2="28" stroke="#ddd" stroke-width=".5"/>
        <rect x="4" y="10" width="3" height="18" fill="#f8b134"/><rect x="8" y="16" width="3" height="12" fill="#2f3439"/><rect x="12" y="20" width="3" height="8" fill="#8f969c"/>
        <rect x="20" y="18" width="3" height="10" fill="#f8b134"/><rect x="24" y="14" width="3" height="14" fill="#2f3439"/><rect x="28" y="21" width="3" height="7" fill="#8f969c"/>
        <rect x="36" y="16" width="3" height="12" fill="#f8b134"/><rect x="40" y="22" width="3" height="6" fill="#2f3439"/><rect x="44" y="8" width="3" height="20" fill="#8f969c"/>
      </svg>
      <div class="page"></div>
    </div>

    <!-- 9 learning topic stats -->
    <div class="slide">
      <span class="tag"><b></b>MARINA HOLT</span>
      <div class="abs ph" style="left:8px;top:8px;width:160px;height:50px;background:linear-gradient(135deg,#5d4a38,#2a231d)" role="img" aria-label="Photo of an open book in a library"></div>
      <div class="kick" style="left:18px;top:40px"><i></i><i></i><i></i>Training Template</div>
      <div class="ttl light" style="left:18px;top:44px">Learning Topic</div>
      <div class="abs" style="left:8px;top:62px;width:48px"><div class="lab">Description</div><div class="t">A short paragraph about the learning topic.</div></div>
      <div class="abs big" style="left:66px;top:65px;width:14px;height:14px;background:var(--orange);font-size:4px;line-height:14px">1.5K</div>
      <div class="abs" style="left:83px;top:66px;width:30px"><div class="lab" style="font-size:2.8px">New Books</div><div class="t">Short note on this point.</div></div>
      <div class="abs big" style="left:117px;top:65px;width:14px;height:14px;background:var(--ink);font-size:4px;line-height:14px">164</div>
      <div class="abs" style="left:134px;top:66px;width:30px"><div class="lab d" style="font-size:2.8px">Visitors</div><div class="t">Short note on this point.</div></div>
      <div class="page"></div>
    </div>

    <!-- 10 traditional single text -->
    <div class="slide">
      <span class="tag"><b></b>MARINA HOLT</span>
      <div class="kick"><i></i><i></i><i></i>Training Template</div>
      <div class="ttl">Traditional Single Text</div>
      <div class="abs" style="left:8px;top:25px;font-size:2.8px;font-weight:700;color:var(--ink)">Study hard so that you can master technology, which allows us to master nature.</div>
      <div class="abs" style="left:8px;top:30px;width:160px;height:.6px;background:var(--orange)"></div>
      <div class="abs t" style="left:8px;top:34px;width:160px">A short paragraph of body text for this slide sits here and continues.<br><span style="color:var(--orange)">✓</span> A short checked point.<br><span style="color:var(--orange)">✓</span> A short checked point.<br><span style="color:var(--orange)">✓</span> A short checked point.<br>A short paragraph of body text for this slide sits here and continues.</div>
      <div class="page"></div>
    </div>

    <!-- 11 our vision -->
    <div class="slide">
      <span class="tag"><b></b>MARINA HOLT</span>
      <div class="kick" style="left:14px;top:14px"><i></i><i></i><i></i>Training Template</div>
      <div class="ttl" style="left:14px;top:18px">Our Vision<br>Topic</div>
      <div class="abs" style="left:14px;top:44px;width:40px"><div class="lab">Description</div><div class="t">Short note on this point.</div></div>
      <div class="abs" style="left:14px;top:64px;width:40px"><div class="lab d">Description</div><div class="t">Short note on this point.</div></div>
      <div class="abs" style="left:88px;top:14px;width:74px;height:74px;border-radius:50%;background:#f1f2f3"></div>
      <div class="abs ph-cool" style="left:95px;top:21px;width:60px;height:60px;border-radius:50%" role="img" aria-label="Photo of an empty classroom"></div>
      <div class="abs" style="left:66px;top:62px;width:62px;height:37px;background:var(--orange);padding:4px"><div class="lab w" style="font-size:2.7px">I know my choices will be creative so long as I follow my heart.</div></div>
      <div class="page"></div>
    </div>

    <!-- 12 timeline 2016-2018 -->
    <div class="slide">
      <span class="tag"><b></b>MARINA HOLT</span>
      <div class="kick"><i></i><i></i><i></i>Training Template</div>
      <div class="ttl">Timeline Models</div>
      <div class="year" style="left:38px;top:28px">2016</div><div class="year" style="left:91px;top:28px">2017</div><div class="year" style="left:143px;top:28px;color:var(--grey)">2018</div>
      <div class="abs" style="left:20px;top:45px;width:150px;height:.6px;background:#eee"></div>
      <div class="para" style="left:30px;top:40px;background:var(--orange)"></div>
      <div class="arrow" style="left:61px;top:44px;width:9px"></div>
      <div class="para" style="left:83px;top:40px;background:var(--orange)"></div>
      <div class="arrow" style="left:114px;top:44px;width:9px"></div>
      <div class="para" style="left:135px;top:40px;background:var(--grey)"></div>
      <div class="abs" style="left:22px;top:60px;width:36px;text-align:center"><div class="lab">Description</div><div class="t">Short note on this point.</div></div>
      <div class="abs" style="left:75px;top:60px;width:36px;text-align:center"><div class="lab">Description</div><div class="t">Short note on this point.</div></div>
      <div class="abs" style="left:127px;top:60px;width:36px;text-align:center"><div class="lab" style="color:var(--grey)">Description</div><div class="t">Short note on this point.</div></div>
      <div class="page"></div>
    </div>

    <!-- 13 timeline 2019-2021 -->
    <div class="slide">
      <span class="tag"><b></b>MARINA HOLT</span>
      <div class="year" style="left:30px;top:28px;color:var(--ink)">2019</div><div class="year" style="left:83px;top:28px;color:var(--ink)">2020</div><div class="year" style="left:135px;top:28px;color:var(--ink)">2021</div>
      <div class="para" style="left:22px;top:40px;background:var(--ink)"></div>
      <div class="arrow k" style="left:53px;top:44px;width:9px"></div>
      <div class="para" style="left:75px;top:40px;background:var(--ink)"></div>
      <div class="arrow k" style="left:106px;top:44px;width:9px"></div>
      <div class="para" style="left:127px;top:40px;background:#151719"></div>
      <div class="abs" style="left:14px;top:60px;width:36px;text-align:center"><div class="lab d">Description</div><div class="t">Short note on this point.</div></div>
      <div class="abs" style="left:67px;top:60px;width:36px;text-align:center"><div class="lab d">Description</div><div class="t">Short note on this point.</div></div>
      <div class="abs" style="left:119px;top:60px;width:36px;text-align:center"><div class="lab d">Description</div><div class="t">Short note on this point.</div></div>
      <div class="page"></div>
    </div>

    <!-- 14 learning topic dark -->
    <div class="slide ph-dark" role="img" aria-label="Dark photo of a person at a desk">
      <span class="tag"><b></b>MARINA HOLT</span>
      <div class="kick" style="top:7px;color:#ccc"><i></i><i></i><i></i>Training Template</div>
      <div class="ttl light" style="top:11px">Learning Topic</div>
      <div class="abs" style="left:16px;top:30px;width:42px"><div class="lab">Certificated</div><div class="t w">Short note on this point.</div></div>
      <div class="abs" style="left:68px;top:30px;width:42px"><div class="lab">Awards</div><div class="t w">Short note on this point.</div></div>
      <div class="abs" style="left:120px;top:30px;width:42px"><div class="lab" style="color:#aaa">Favorite</div><div class="t w">Short note on this point.</div></div>
      <div class="abs" style="left:18px;top:54px;width:150px;height:38px;background:#2a2f33;padding:4px 8px"><div class="lab w">Description</div><div class="t w">A short paragraph describing the learning topic.</div></div>
      <div class="abs" style="left:18px;top:54px;width:2px;height:24px;background:var(--orange)"></div>
      <div class="pill" style="left:30px;top:83px;width:18px">Learn More</div>
      <div class="abs t w" style="left:54px;top:84px">For more information</div>
      <div class="abs" style="left:0;top:92px;width:176px;height:7px;background:#fff"></div>
    </div>

    <!-- 15 quote dark -->
    <div class="slide ph-dark" role="img" aria-label="Dark photo of a training room">
      <span class="tag"><b></b>MARINA HOLT</span>
      <div class="abs" style="left:12px;top:46px;font-family:Oswald,sans-serif;font-size:12px;color:#fff">”</div>
      <div class="abs" style="left:28px;top:50px;width:110px;font-family:Oswald,sans-serif;font-size:4.3px;color:#fff;line-height:1.25">Study hard so that you can master technology, which allows us to master nature.</div>
      <div class="pill" style="left:28px;top:64px;width:20px">Learn More</div>
    </div>

    <!-- 16 topic models band -->
    <div class="slide">
      <span class="tag"><b></b>MARINA HOLT</span>
      <div class="kick"><i></i><i></i><i></i>Training Template</div>
      <div class="ttl">Topic Models</div>
      <div class="abs ph" style="left:8px;top:26px;width:160px;height:52px" role="img" aria-label="Photo of people working with books and laptops"></div>
      <div class="abs" style="left:55px;top:26px;width:56px;height:26px;background:var(--ink);padding:3px 6px"><div class="lab w">Description</div><div class="t w">Short note on this point.</div></div>
      <div class="abs" style="left:8px;top:52px;width:50px;height:26px;background:var(--orange);padding:3px 6px"><div class="lab w">Description</div><div class="t w">Short note on this point.</div></div>
      <div class="abs" style="left:112px;top:52px;width:56px;height:26px;background:#1c1f22;padding:3px 6px"><div class="lab w">Description</div><div class="t w">Short note on this point.</div></div>
      <div class="page"></div>
    </div>

    <!-- 17 topic models cards -->
    <div class="slide">
      <span class="tag"><b></b>MARINA HOLT</span>
      <div class="kick"><i></i><i></i><i></i>Training Template</div>
      <div class="ttl">Topic Models</div>
      <div class="abs" style="left:10px;top:26px;width:50px;height:58px;box-shadow:0 0 2px rgba(0,0,0,.2)"><div class="ph-cool" style="height:24px" role="img" aria-label="Photo of a laptop on a desk"></div><div style="padding:2px 3px"><div class="lab d" style="font-size:2.6px">Wonderful College for Study and Learn</div><div class="t">Short note on this point.</div></div></div>
      <div class="abs" style="left:63px;top:26px;width:50px;height:58px;box-shadow:0 0 2px rgba(0,0,0,.2)"><div class="ph" style="height:24px" role="img" aria-label="Photo of a laptop and notes"></div><div style="padding:2px 3px"><div class="lab d" style="font-size:2.6px">Creative Learning Method is New Style</div><div class="t">Short note on this point.</div></div></div>
      <div class="abs" style="left:116px;top:26px;width:50px;height:58px;box-shadow:0 0 2px rgba(0,0,0,.2)"><div class="ph-dark" style="height:24px" role="img" aria-label="Photo of a camera on a tripod"></div><div style="padding:2px 3px"><div class="lab d" style="font-size:2.6px">Experienced Teacher and Mentor for Study</div><div class="t">Short note on this point.</div></div></div>
      <div class="page"></div>
    </div>

    <!-- 18 doughnut chart -->
    <div class="slide">
      <span class="tag"><b></b>MARINA HOLT</span>
      <div class="kick" style="top:14px"><i></i><i></i><i></i>Training Template</div>
      <div class="ttl" style="top:18px">Doughnut Chart</div>
      <div class="abs t" style="left:8px;top:30px;width:60px">A short paragraph on the chart data.</div>
      <svg class="abs" style="left:18px;top:44px" width="46" height="46" viewBox="0 0 46 46" role="img" aria-label="Doughnut chart">
        <circle cx="23" cy="23" r="15" fill="none" stroke="#2f3439" stroke-width="8"/>
        <circle cx="23" cy="23" r="15" fill="none" stroke="#f8b134" stroke-width="8" stroke-dasharray="24 70.2" transform="rotate(-160 23 23)"/>
        <circle cx="23" cy="23" r="15" fill="none" stroke="#eceef0" stroke-width="8" stroke-dasharray="8 86" transform="rotate(-205 23 23)"/>
      </svg>
      <div class="abs t" style="left:66px;top:60px">■ Item One<br>■ Item Two<br>■ Item Three</div>
      <div class="abs" style="left:94px;top:18px;width:48px;height:70px;background:#e3e5e7;border-radius:2px"></div>
      <div class="abs ph" style="left:112px;top:24px;width:30px;height:58px" role="img" aria-label="Photo on a tablet screen"></div>
      <div class="sq o" style="left:132px;top:26px"></div><div class="sq k" style="left:132px;top:45px"></div><div class="sq k" style="left:132px;top:64px;background:#151719"></div>
      <div class="abs" style="left:142px;top:26px;width:28px"><div class="lab">Description</div><div class="t">Short note on this point.</div><div class="lab d" style="margin-top:5px">Description</div><div class="t">Short note on this point.</div><div class="lab d" style="margin-top:5px">Description</div><div class="t">Short note on this point.</div></div>
      <div class="page"></div>
    </div>

    <!-- 19 process models -->
    <div class="slide">
      <span class="tag"><b></b>MARINA HOLT</span>
      <div class="kick"><i></i><i></i><i></i>Training Template</div>
      <div class="ttl">Process Models</div>
      <div class="year" style="left:19px;top:26px">01.</div><div class="year" style="left:52px;top:26px">02.</div><div class="year" style="left:85px;top:26px;color:var(--grey)">03.</div><div class="year" style="left:118px;top:26px;color:var(--ink)">04.</div><div class="year" style="left:151px;top:26px;color:var(--ink)">05</div>
      <div class="abs" style="left:8px;top:36px;width:25px;height:24px;background:var(--orange)"></div>
      <div class="abs" style="left:41px;top:36px;width:25px;height:24px;background:var(--orange)"></div>
      <div class="abs" style="left:74px;top:36px;width:25px;height:24px;background:var(--grey)"></div>
      <div class="abs" style="left:107px;top:36px;width:25px;height:24px;background:var(--slate)"></div>
      <div class="abs" style="left:140px;top:36px;width:25px;height:24px;background:var(--ink)"></div>
      <div class="abs" style="left:6px;top:64px;width:29px;text-align:center"><div class="lab">Description</div><div class="t">Short note on this point.</div></div>
      <div class="abs" style="left:39px;top:64px;width:29px;text-align:center"><div class="lab">Description</div><div class="t">Short note on this point.</div></div>
      <div class="abs" style="left:72px;top:64px;width:29px;text-align:center"><div class="lab d">Description</div><div class="t">Short note on this point.</div></div>
      <div class="abs" style="left:105px;top:64px;width:29px;text-align:center"><div class="lab d">Description</div><div class="t">Short note on this point.</div></div>
      <div class="abs" style="left:138px;top:64px;width:29px;text-align:center"><div class="lab d">Description</div><div class="t">Short note on this point.</div></div>
      <div class="page"></div>
    </div>

    <!-- 20 level models -->
    <div class="slide">
      <span class="tag"><b></b>MARINA HOLT</span>
      <div class="kick"><i></i><i></i><i></i>Training Template</div>
      <div class="ttl">Level Models</div>
      <div class="abs" style="left:12px;top:36px;width:50px;font-family:Oswald,sans-serif;font-size:4px;color:var(--ink)">Learn with Creative Method</div>
      <div class="abs t" style="left:12px;top:50px;width:46px">A short paragraph on this creative method.</div>
      <div class="pill dark" style="left:12px;top:68px;width:28px">www.yourwebsite.com</div>
      <div class="sq o" style="left:114px;top:22px;width:8px;height:8px"></div><div class="sq o" style="left:114px;top:40px;width:8px;height:8px"></div><div class="sq k" style="left:114px;top:58px;width:8px;height:8px"></div><div class="sq k" style="left:114px;top:76px;width:8px;height:8px;background:#151719"></div>
      <div class="abs" style="left:126px;top:21px;width:44px"><div class="lab">Description</div><div class="t">Short note on this point.</div></div>
      <div class="abs" style="left:126px;top:39px;width:44px"><div class="lab">Description</div><div class="t">Short note on this point.</div></div>
      <div class="abs" style="left:126px;top:57px;width:44px"><div class="lab d">Description</div><div class="t">Short note on this point.</div></div>
      <div class="abs" style="left:126px;top:75px;width:44px"><div class="lab d">Description</div><div class="t">Short note on this point.</div></div>
    </div>

    <!-- 21 pie chart concept -->
    <div class="slide">
      <span class="tag"><b></b>MARINA HOLT</span>
      <div class="kick"><i></i><i></i><i></i>Training Template</div>
      <div class="ttl">Pie Chart Concept</div>
      <svg class="abs" style="left:0;top:24px" width="176" height="40" viewBox="0 0 176 40" role="img" aria-label="Four ring charts">
        <g fill="none" stroke-width="3">
          <circle cx="28" cy="18" r="9" stroke="#e3e5e7"/><circle cx="28" cy="18" r="9" stroke="#f8b134" stroke-dasharray="15.8 56.5" transform="rotate(-90 28 18)"/>
          <circle cx="67" cy="18" r="9" stroke="#e3e5e7"/><circle cx="67" cy="18" r="9" stroke="#f39c12" stroke-dasharray="41.3 56.5" transform="rotate(-90 67 18)"/>
          <circle cx="108" cy="18" r="9" stroke="#e3e5e7"/><circle cx="108" cy="18" r="9" stroke="#6e767d" stroke-dasharray="41.8 56.5" transform="rotate(-90 108 18)"/>
          <circle cx="149" cy="18" r="9" stroke="#e3e5e7"/><circle cx="149" cy="18" r="9" stroke="#1c1f22" stroke-dasharray="15.3 56.5" transform="rotate(-90 149 18)"/>
        </g>
      </svg>
      <div class="abs big" style="left:22px;top:56px;width:12px;height:5px;background:var(--orange);font-size:2.6px;line-height:5px">28%</div>
      <div class="abs big" style="left:61px;top:56px;width:12px;height:5px;background:var(--orange-deep);font-size:2.6px;line-height:5px">73%</div>
      <div class="abs big" style="left:102px;top:56px;width:12px;height:5px;background:var(--slate);font-size:2.6px;line-height:5px">74%</div>
      <div class="abs big" style="left:143px;top:56px;width:12px;height:5px;background:var(--ink);font-size:2.6px;line-height:5px">27%</div>
      <div class="abs" style="left:12px;top:64px;width:32px;text-align:center"><div class="lab">Description</div><div class="t">Short note on this point.</div></div>
      <div class="abs" style="left:51px;top:64px;width:32px;text-align:center"><div class="lab">Description</div><div class="t">Short note on this point.</div></div>
      <div class="abs" style="left:92px;top:64px;width:32px;text-align:center"><div class="lab d">Description</div><div class="t">Short note on this point.</div></div>
      <div class="abs" style="left:133px;top:64px;width:32px;text-align:center"><div class="lab d">Description</div><div class="t">Short note on this point.</div></div>
      <div class="page"></div>
    </div>

    <!-- 22 maps concept -->
    <div class="slide">
      <span class="tag"><b></b>MARINA HOLT</span>
      <div class="kick" style="left:8px;top:20px"><i></i><i></i><i></i>Training Template</div>
      <div class="ttl" style="left:8px;top:24px">Maps Concept</div>
      <div class="abs t" style="left:8px;top:36px;width:50px">A short paragraph on student reach.</div>
      <div class="abs lab" style="left:8px;top:50px;font-size:2.6px">Male Students</div>
      <div class="abs" style="left:8px;top:55px;font-size:4px;letter-spacing:-.3px;color:var(--orange)">▮▮▮▮▮▮<span style="color:#ccc">▮▮▮▮</span> <span style="font-size:3px;font-weight:700">60%</span></div>
      <div class="abs lab d" style="left:8px;top:66px;font-size:2.6px">Female Students</div>
      <div class="abs" style="left:8px;top:71px;font-size:4px;letter-spacing:-.3px;color:var(--ink)">▮▮▮▮▮▮▮▮▮<span style="color:#ccc">▮</span> <span style="font-size:3px;font-weight:700">90%</span></div>
      <div class="abs" style="left:92px;top:16px;width:74px;height:70px;background:#dfe2e5;border-radius:40% 50% 45% 40%" role="img" aria-label="Map of a continent"></div>
      <div class="abs big" style="left:92px;top:24px;width:30px;height:30px;border-radius:50%;background:var(--ink);padding-top:8px;font-size:7px;line-height:1">843K<br><span style="font-size:2px">Female Students</span></div>
      <div class="abs big" style="left:117px;top:44px;width:26px;height:26px;border-radius:50%;background:var(--orange);padding-top:8px;font-size:5.5px;line-height:1">472K<br><span style="font-size:2px">Male Students</span></div>
      <div class="page"></div>
    </div>

    <!-- 23 quote models -->
    <div class="slide">
      <span class="tag"><b></b>MARINA HOLT</span>
      <div class="kick" style="left:72px;top:8px"><i></i><i></i><i></i>Training Template</div>
      <div class="ttl" style="left:0;width:176px;text-align:center;top:14px">Quote Models</div>
      <div class="abs" style="left:0;top:27px;width:176px;height:50px;background:var(--slate)"></div>
      <div class="abs" style="left:20px;top:37px;width:136px;text-align:center;font-family:Oswald,sans-serif;font-size:4.3px;line-height:1.3;color:#fff">“A single conversation across the table with a wise man is better than ten years mere study of books.”</div>
      <div class="abs t w" style="left:0;width:176px;top:66px;text-align:center">Elena Marsh</div>
      <div class="page"></div>
    </div>

    <!-- 24 your contact -->
    <div class="slide">
      <div class="abs" style="left:0;top:0;width:176px;height:99px;background:linear-gradient(135deg,#c8ccd0,#a8aeb3)" role="img" aria-label="Street map background"></div>
      <div class="abs ph" style="left:16px;top:8px;width:64px;height:40px" role="img" aria-label="Photo of a person using a phone at a laptop"></div>
      <div class="abs" style="left:16px;top:48px;width:64px;height:14px;background:var(--ink);padding:3px 4px"><div class="t w">A short note about where we are.</div></div>
      <div class="abs" style="left:80px;top:8px;width:80px;height:82px;background:#fff;padding:4px 10px">
        <div style="font-size:2.2px;color:var(--grey)">Training Template</div>
        <div style="font-family:Oswald,sans-serif;font-size:8px;color:var(--ink)">Your Contact</div>
        <div class="t">A short note on how to reach us.</div>
        <div class="lab d" style="font-size:2.6px;margin-top:3px">Need more help?</div>
        <div class="t">○ Call us any day<br>○ Write to our team<br>○ Visit our office</div>
      </div>
      <div class="pill dark" style="left:91px;top:76px;width:18px">Ask more</div>
      <div class="page"></div>
    </div>

    <!-- 25 thank you -->
    <div class="slide ph-dark" role="img" aria-label="Dark photo of a smiling person with a notebook">
      <div class="abs" style="left:22px;top:30px;display:flex;align-items:center;gap:1.5px;font-family:Oswald,sans-serif;font-size:3px;color:var(--orange)"><span style="width:5px;height:5px;border-radius:50%;border:.8px solid var(--orange)"></span>MARINA HOLT</div>
      <div class="kick" style="left:22px;top:37px;color:#ccc"><i></i><i></i><i></i>Training Template</div>
      <div class="abs" style="left:22px;top:40px;font-family:Oswald,sans-serif;font-weight:500;font-size:14px;color:#fff">Thank You</div>
      <div class="pill" style="left:22px;top:60px;width:30px">www.yourwebsite.com</div>
    </div>
  </section>
</main>
</body>
</html>
```